Business Card Design

I am a criminologist running a research and consultancy business on my own (PKConsultants)
I specialise in looking at fraud and other white-collar crimes. Also governance issues..
I would like a professional business card that would be appropriate both in the academic and business sector as I straddle both sectors. Normal shape - not square.
I am interested in seeing border Word Cloud type projects - black on white or white on black..
Example key words would be fraud, research, qualitative, interviews, quantitative, white-collar, reports, government, surveys, sample, governance, assurance, crime, offenders, prison etc (I can provide a full list if this is the option I go for). I also like Word Cloud borders as attached.
I am also interested in seeing other style business cards. Preferably one colour, plus black and white.
In particular I like black backgrounds with coloured words etc - colours like lime green are good.
I also like blues - especially teal if a traditional white background is chosen.
I don't have a logo - unless anyone can think of anything that's particularly appropriate.
Graphics can be used but they would be simple and stylish (dots, squares, lines, curves etc)
I would like the design to translate simply for a header for a website or blog.
My current website is www.pelling-hurst.com but is out of date in terms of what I do and design.
I have attached a number of things that have caught my eye and inspired me.
I have asked for a one-sided business card in the first instance - however if someone comes up with a good cloud design that might go on one side, I would consider a two-sided one.
Design can be landscape or portrait.
Kind Regards
Meg
Landscape
Contact Information for Business Card
PKConsultants
Dr Margery Pelling-Hurst, MSc, BSc, **
42 Brindle Wold
Stone, Staffordshire
KX27 4QD
+44(0)1620 482917
+44(0)7531 804152
www.pelling-hurst.com
margery@pelling-hurst.com

```html
<!DOCTYPE html>
<html lang="en">
<head>
<meta charset="utf-8">
<title>PKConsultants – Business Card</title>
<link rel="stylesheet" href="https://fonts.googleapis.com/css2?family=Marcellus+SC&family=Lora:wght@400&display=swap">
<style>
  :root {
    --page-bg: #dcdcdc;
    --card-black: #0a0a0a;
    --card-sheen: #262626;
    --lime: #2fb34a;
    --lime-bright: #41c052;
    --forest: #137a38;
    --forest-deep: #04360f;
    --web-green: #1a9e3f;
    --paper: #ffffff;
    --ink-light: #f4f4f4;
  }
  html, body {
    margin: 0;
    padding: 0;
    width: 1200px;
    height: 801px;
    overflow: hidden;
    background: var(--page-bg);
  }
  .card {
    position: absolute;
    left: 40px;
    top: 80px;
    width: 1120px;
    height: 640px;
    overflow: hidden;
    background:
      radial-gradient(ellipse 70% 55% at 55% 30%, var(--card-sheen) 0%, rgba(20,20,20,0.6) 45%, rgba(0,0,0,0) 80%),
      repeating-linear-gradient(0deg, rgba(255,255,255,0.018) 0 1px, rgba(0,0,0,0) 1px 3px),
      var(--card-black);
    box-shadow: 0 6px 18px rgba(0,0,0,0.35);
  }
  .card__bands {
    position: absolute;
    left: 0;
    top: 0;
    width: 1120px;
    height: 640px;
  }
  .company-name {
    position: absolute;
    left: 61px;
    top: 52px;
    margin: 0;
    font-family: "Marcellus SC", serif;
    font-weight: 400;
    font-size: 72px;
    letter-spacing: 3px;
    color: var(--lime);
    line-height: 1;
  }
  .person {
    position: absolute;
    left: 61px;
    top: 224px;
    margin: 0;
    font-family: "Marcellus SC", serif;
    color: var(--web-green);
    line-height: 1;
  }
  .person__name {
    display: block;
    font-size: 40px;
    letter-spacing: 1px;
  }
  .person__credentials {
    display: block;
    margin-top: 16px;
    font-size: 29px;
    letter-spacing: 1px;
  }
  .address {
    position: absolute;
    right: 45px;
    top: 422px;
    margin: 0;
    font-family: "Lora", serif;
    font-style: normal;
    font-size: 28px;
    line-height: 38px;
    color: var(--ink-light);
    text-align: right;
  }
  .contact {
    position: absolute;
    left: 57px;
    top: 496px;
    margin: 0;
    padding: 0;
    list-style: none;
    font-family: "Lora", serif;
    font-size: 27px;
    line-height: 37.5px;
    color: var(--ink-light);
  }
  .website {
    position: absolute;
    right: 45px;
    top: 562px;
    margin: 0;
    font-family: "Lora", serif;
    font-size: 34px;
    line-height: 1.2;
    color: var(--web-green);
  }
</style>
</head>
<body>
  <main class="card">
    <svg class="card__bands" viewBox="0 0 1120 640" aria-hidden="true">
      <defs>
        <linearGradient id="contactBandFill" x1="0" y1="0" x2="1" y2="0">
          <stop offset="0" stop-color="var(--lime-bright)"/>
          <stop offset="0.45" stop-color="var(--lime)"/>
          <stop offset="1" stop-color="var(--forest)"/>
        </linearGradient>
      </defs>
      <polygon class="band band--contact" points="0,473 515,473 456,640 0,640" fill="url(#contactBandFill)"/>
      <polygon class="band band--fold" points="515,473 548,508 456,640" fill="var(--forest-deep)"/>
      <polygon class="band band--web" points="548,508 1120,508 1120,640 456,640" fill="var(--paper)"/>
    </svg>

    <h1 class="company-name">PKCONSULTANTS</h1>

    <p class="person">
      <span class="person__name">Dr Margery Pelling</span>
      <span class="person__credentials">Hurst, MSc, BSc</span>
    </p>

    <address class="address">42 Brindle Wold Stone,<br>Staffordshire KX27 4QD</address>

    <ul class="contact">
      <li class="contact__phone">+44(0)1620 482917</li>
      <li class="contact__mobile">+44(0)7531 804152</li>
      <li class="contact__email">margery@pelling-hurst.com</li>
    </ul>

    <p class="website">www.pelling-hurst.com</p>
  </main>
</body>
</html>
```